Goldschmiede sucht Flyer mit GUtschein abriss
Zielgruppe
ICh bin ein Goldschmied in Saarbrücken Trier und Mainz und mache jegliche Dienstleistungen eines Goldschmiedes.Es sollen noch mit ein paar passenden Fotos gearbeitet werden.
Aufgabenstellung
Ich suche einen Flyer für meine Goldschmiede vorhandene Punkte sollen sein.
Reparaturen aller Art , Ringweitenänderung, Löten , Polieren / Aufarbeiten , Neuanfertigung nach Wunsch ,Rhodienieren , Gravieren , usw.
Der Flyer soll am unteren Rand die Möglichkeit haben, abgeschnitten zu werden dort soll ein Gutschein entstehen zb. mit 20 % Rabatt.
( der Abriss soll nummeriert werden damit niemand kopiert oder mehrfach abgibt )
Auf der Internetseite können Sie sich meine Firmenfarben ansehen in diesen Farben soll auch das Flyer-Design sein.
Bei der Adresse sollen alle drei Filialen angegeben werden.

```html
<!DOCTYPE html>
<html lang="de">
<head>
<meta charset="utf-8">
<title>Goldschmiede Flyer</title>
<link rel="stylesheet" href="https://fonts.googleapis.com/css2?family=Montserrat:wght@400;500;600;700&display=swap">
<style>
  :root {
    --gold: #b39b57;
    --gold-light: #e6c770;
    --dark: #4a4a4c;
    --paper: #f6f6f4;
    --white: #ffffff;
    --stage: #e9e4dc;
  }
  * { margin: 0; padding: 0; box-sizing: border-box; }
  html, body { width: 1200px; height: 1200px; overflow: hidden; }
  body { background: var(--stage); font-family: "Montserrat", sans-serif; color: var(--dark); }

  .flyer {
    position: absolute; left: 206px; top: 41px; width: 788px; height: 1118px;
    background: var(--white); box-shadow: 0 6px 18px rgba(0,0,0,.18);
  }
  .rule { position: absolute; left: 0; width: 100%; height: 6px;
    background: linear-gradient(90deg, var(--gold), var(--gold-light) 50%, var(--gold)); }
  .rule--top { top: 19px; }
  .rule--head { top: 243px; }
  .rule--mid { top: 797px; }
  .rule--bottom { top: 1108px; }

  .header { position: absolute; top: 32px; left: 0; width: 100%; height: 204px; background: var(--dark);
    display: flex; flex-direction: column; align-items: center; justify-content: center; }
  .brand-name { color: var(--gold); font-weight: 500; font-size: 40px; letter-spacing: 1px; line-height: 1.1; }
  .brand-sub { color: var(--gold); font-weight: 500; font-size: 22px; letter-spacing: 4px; margin-top: 8px; }

  .services-area { position: absolute; top: 250px; left: 0; width: 100%; height: 547px; background: var(--paper); }
  .services { position: absolute; left: 36px; top: 86px; list-style: none; }
  .services li { display: flex; align-items: center; height: 37.6px; font-weight: 600; font-size: 19.5px; letter-spacing: .6px; }
  .services li svg { width: 22px; height: 12px; margin-right: 12px; }
  .services .gold { color: var(--gold); }
  .services .dark { color: var(--dark); }

  .rings-photo { position: absolute; left: 449px; top: 249px; width: 339px; height: 298px;
    background: radial-gradient(ellipse at 55% 50%, #d9a13c 0%, #b88a4a 35%, #c9b99a 60%, var(--paper) 80%); }

  .branches { position: absolute; top: 804px; left: 0; width: 100%; height: 127px; }
  .branch { position: absolute; top: 24px; font-size: 16px; line-height: 20.5px; color: var(--dark); }
  .branch h3 { color: var(--gold); font-size: 16px; font-weight: 700; letter-spacing: .5px; margin-bottom: 1px; }
  .branch--1 { left: 45px; } .branch--2 { left: 314px; } .branch--3 { left: 596px; }
  .divider { position: absolute; top: 34px; width: 1.5px; height: 60px; background: var(--gold); }
  .divider--1 { left: 250px; } .divider--2 { left: 537px; }

  .coupon { position: absolute; top: 931px; left: 0; width: 100%; height: 127px; }
  .jewelry-photo { position: absolute; left: 0; top: 0; width: 378px; height: 127px;
    background: linear-gradient(100deg, #6b4d1c, #c89a3a 40%, #8a6524 70%, #d6b25a); }
  .coupon-panel { position: absolute; left: 390px; top: 0; width: 398px; height: 127px; background: var(--dark); }
  .coupon-tag { position: absolute; left: 360px; top: 0; width: 214px; height: 86px; }
  .cut-line { position: absolute; left: 530px; top: -2px; width: 250px; border-top: 2px dashed var(--white); }
  .scissors { position: absolute; left: 736px; top: -16px; width: 30px; height: 26px; }
  .discount { position: absolute; left: 390px; top: 10px; color: var(--white); font-weight: 700; font-size: 52px; letter-spacing: 1px; }
  .coupon-number { position: absolute; left: 412px; top: 96px; color: var(--white); font-size: 17px; font-weight: 500; letter-spacing: .5px; }
  .coupon-title { position: absolute; left: 583px; top: 12px; color: var(--white); font-size: 44px; font-weight: 500; letter-spacing: 2px; line-height: 1; }
  .coupon-text { position: absolute; left: 583px; top: 64px; color: var(--white); font-size: 20px; font-weight: 500; letter-spacing: 1.3px; line-height: 25px; }

  .hours { position: absolute; top: 1070px; left: 0; width: 100%; text-align: center; font-size: 14.5px; font-weight: 700; letter-spacing: .3px; color: var(--dark); }
  .hours span { color: var(--gold); }
</style>
</head>
<body>
<div class="flyer">
  <div class="rule rule--top"></div>
  <header class="header">
    <div class="brand-name">Matthias Lorenz</div>
    <div class="brand-sub">Goldschmiede</div>
  </header>
  <div class="rule rule--head"></div>

  <section class="services-area">
    <ul class="services">
      <li class="gold"><svg viewBox="0 0 22 12"><path d="M2 6h16M13 1l5 5-5 5" fill="none" stroke="currentColor" stroke-width="2"/></svg>REPARATUREN ALLER ART</li>
      <li class="dark"><svg viewBox="0 0 22 12"><path d="M2 6h16M13 1l5 5-5 5" fill="none" stroke="currentColor" stroke-width="2"/></svg>RINGWEITENÄNDERUNG</li>
      <li class="gold"><svg viewBox="0 0 22 12"><path d="M2 6h16M13 1l5 5-5 5" fill="none" stroke="currentColor" stroke-width="2"/></svg>LÖTEN</li>
      <li class="dark"><svg viewBox="0 0 22 12"><path d="M2 6h16M13 1l5 5-5 5" fill="none" stroke="currentColor" stroke-width="2"/></svg>POLIEREN / AUFARBEITEN</li>
      <li class="gold"><svg viewBox="0 0 22 12"><path d="M2 6h16M13 1l5 5-5 5" fill="none" stroke="currentColor" stroke-width="2"/></svg>NEUANFERTIGUNG NACH WUNSCH</li>
      <li class="dark"><svg viewBox="0 0 22 12"><path d="M2 6h16M13 1l5 5-5 5" fill="none" stroke="currentColor" stroke-width="2"/></svg>RHODENIEREN</li>
      <li class="gold"><svg viewBox="0 0 22 12"><path d="M2 6h16M13 1l5 5-5 5" fill="none" stroke="currentColor" stroke-width="2"/></svg>GRAVIEREN</li>
      <li class="dark"><svg viewBox="0 0 22 12"><path d="M2 6h16M13 1l5 5-5 5" fill="none" stroke="currentColor" stroke-width="2"/></svg>UND VIELES MEHR</li>
    </ul>
    <div class="rings-photo" role="img" aria-label="Foto: zwei alte gravierte Eheringe aus Gold"></div>
  </section>
  <div class="rule rule--mid"></div>

  <section class="branches">
    <div class="branch branch--1"><h3>SAARBRÜCKEN</h3>Lindenweg 4<br>66111 Saarbrücken<br>Tel: 0681 - 12 345 670</div>
    <div class="divider divider--1"></div>
    <div class="branch branch--2"><h3>TRIER</h3>Am Marktplatz 7<br>54290 Trier<br>Tel: 0651 - 23 456 780</div>
    <div class="divider divider--2"></div>
    <div class="branch branch--3"><h3>MAINZ</h3>Rosengasse 22<br>55116 Mainz<br>Tel: 06131 - 345 67 89</div>
  </section>

  <section class="coupon">
    <div class="jewelry-photo" role="img" aria-label="Foto: Goldschmuck mit Perle und Ketten"></div>
    <div class="coupon-panel"></div>
    <svg class="coupon-tag" viewBox="0 0 214 86" aria-hidden="true">
      <defs><linearGradient id="tagGold" x1="0" x2="1"><stop offset="0" stop-color="#c9ad62"/><stop offset=".5" stop-color="#f0d488"/><stop offset="1" stop-color="#b39b57"/></linearGradient></defs>
      <polygon points="0,0 188,0 214,43 188,86 0,86" fill="url(#tagGold)"/>
    </svg>
    <div class="cut-line"></div>
    <svg class="scissors" viewBox="0 0 30 26" aria-hidden="true">
      <g fill="none" stroke="#b39b57" stroke-width="2"><circle cx="6" cy="20" r="4"/><circle cx="24" cy="20" r="4"/><path d="M9 17L24 2M21 17L6 2"/></g>
    </svg>
    <div class="discount">20 %</div>
    <div class="coupon-number">NR: 66565</div>
    <div class="coupon-title">RABATT</div>
    <div class="coupon-text">auf alle Gold-<br>schmiedearbeiten</div>
  </section>

  <p class="hours"><span>ÖFFNUNGSZEITEN:</span> MO - FR 9:30 BIS 18:00 UHR UND SA 9:30 BIS 14:00 UHR</p>
  <div class="rule rule--bottom"></div>
</div>
</body>
</html>
```